Colorful Live Music Concert Poster for Tin Harbor

Looking for a portrait oriented "poster" promoting the band's upcoming show at Marlow Lounge on Sunday, 3/22 at 8 pm, and social version (square format for Instagram). <br/><br/>Copy:<br/>Tin Harbor<br/>with The Pale Wires<br/><br/>Marlow Lounge <br/>Sunday, March 22<br/>8 pm<br/><br/>Poster must be consistent with band's overall branding seen on www.tinharborband.example and it's Tunevault page at https://music.example.com/artist/7QxRtaWpLeNmVcz2Ks9DuB?si=381fkTsYpWmaGHeLoRqdXC <br/><br/>BUT, we wouldn't mind taking in a slightly updated direction. A good example is the cover for our recent single Glad Today, which is consistent in theme and color palette while updating the design and color at the same time. <br/><br/>The attached files include some band logo art as well as examples of posters done for prior shows. <br/><br/>The posters need not include photos of the band, but if you are so inclined, we've uploaded some selects as well.<br/><br/>Thank you. <br/><br/>Wendell<br/>Tin Harbor

```html
<!DOCTYPE html>
<html lang="en">
<head>
<meta charset="utf-8">
<title>Tin Harbor with The Pale Wires at Marlow Lounge</title>
<link rel="stylesheet" href="https://fonts.googleapis.com/css2?family=Mulish:wght@400;600;800&display=swap">
<style>
  :root {
    --aqua: #03f6d6;
    --navy: #17197a;
    --amber: #fcae00;
  }
  html, body {
    margin: 0;
    padding: 0;
    overflow: hidden;
    background: var(--aqua);
  }
  .poster {
    position: relative;
    width: 855px;
    height: 1200px;
    overflow: hidden;
    background: var(--aqua);
    color: var(--navy);
    font-family: "Mulish", sans-serif;
  }
  .band-name {
    position: absolute;
    right: 60px;
    top: 74px;
    margin: 0;
    font-size: 43px;
    font-weight: 400;
    letter-spacing: 0.12em;
    line-height: 1;
    text-transform: uppercase;
    white-space: nowrap;
  }
  .socials {
    position: absolute;
    right: 60px;
    top: 143px;
    display: flex;
    gap: 22px;
    margin: 0;
    padding: 0;
    list-style: none;
    font-size: 10px;
    font-weight: 600;
  }
  .socials li {
    display: flex;
    align-items: center;
    gap: 4px;
  }
  .socials .dot {
    width: 14px;
    height: 14px;
    border-radius: 50%;
    background: var(--navy);
  }
  .headliner-mark {
    position: absolute;
    left: 91px;
    top: 430px;
    width: 420px;
  }
  .headliner-mark .sun {
    display: block;
    width: 92px;
    height: 92px;
    border-radius: 50%;
    background: var(--amber);
    margin-left: 120px;
    margin-bottom: 18px;
  }
  .headliner-mark .word {
    display: block;
    font-size: 104px;
    font-weight: 800;
    line-height: 0.98;
    text-transform: uppercase;
    letter-spacing: 0.01em;
  }
  .details {
    position: absolute;
    left: 163px;
    top: 872px;
    margin: 0;
    text-transform: uppercase;
  }
  .details p { margin: 0; white-space: nowrap; }
  .support-intro {
    font-size: 29px;
    font-weight: 400;
    line-height: 1.1;
  }
  .support-act {
    font-size: 47px;
    font-weight: 400;
    line-height: 1.1;
    margin-top: 14px !important;
  }
  .show-date {
    font-size: 33px;
    font-weight: 800;
    line-height: 1.1;
    margin-top: 18px !important;
  }
  .venue {
    font-size: 35px;
    font-weight: 400;
    line-height: 1.1;
    margin-top: 10px !important;
  }
  .address {
    font-size: 19px;
    font-weight: 600;
    line-height: 1.2;
    text-transform: none;
    margin-top: 4px !important;
  }
</style>
</head>
<body>
  <main class="poster">
    <h1 class="band-name">Tin Harbor</h1>
    <ul class="socials">
      <li><span class="dot"></span>@tinharborband</li>
      <li><span class="dot"></span>@tinharborband</li>
      <li><span class="dot"></span>/tinharborband</li>
    </ul>

    <div class="headliner-mark">
      <span class="sun"></span>
      <span class="word">Tin</span>
      <span class="word">Harbor</span>
    </div>

    <section class="details">
      <p class="support-intro">With</p>
      <p class="support-act">The Pale Wires</p>
      <p class="show-date">Sunday, March 22, 8PM</p>
      <p class="venue">Marlow Lounge</p>
      <p class="address">418 W Larkspur Ave. Los Angeles, CA 90031</p>
    </section>
  </main>
</body>
</html>
```